Business Card Design Project_Velmora&Co

Hi,

We need some business cards designed that match the branding of this website: www.velmoraandco-example.com

They should match this branding and include a field for:

Name
Title
Email
Mobile number
Web Address

```html
<!DOCTYPE html>
<html lang="en">
<head>
<meta charset="utf-8">
<title>Velmora&amp;Co Business Card</title>
<link href="https://fonts.googleapis.com/css2?family=Jost:wght@300;400;500;600&display=swap" rel="stylesheet">
<style>
  :root {
    --backdrop: #a7a8ab;
    --card-white: #ffffff;
    --ink: #000000;
    --paper-text: #ffffff;
    --dot-grey: #9a9a9a;
    --shadow: rgba(0, 0, 0, 0.45);
  }
  * { margin: 0; padding: 0; box-sizing: border-box; }
  html, body {
    width: 800px;
    height: 1200px;
    overflow: hidden;
    background: var(--backdrop);
    font-family: "Jost", "Futura", sans-serif;
  }
  .canvas {
    position: relative;
    width: 800px;
    height: 1200px;
  }
  .card {
    position: absolute;
    width: 670px;
    height: 430px;
    box-shadow: 5px 6px 5px var(--shadow);
  }
  .card-front {
    left: 56px;
    top: 56px;
    background: var(--card-white);
  }
  .card-back {
    left: 62px;
    top: 592px;
    width: 667px;
    background: var(--ink);
    display: flex;
    align-items: center;
    justify-content: center;
  }
  .name-tag {
    position: absolute;
    left: 320px;
    top: 52px;
    width: 306px;
    height: 63px;
    background: var(--ink);
    color: var(--paper-text);
    text-align: center;
    padding-top: 3px;
  }
  .name-tag .person-name {
    font-weight: 600;
    font-size: 21px;
    line-height: 27px;
  }
  .name-tag .person-title {
    font-weight: 300;
    font-size: 19px;
    line-height: 27px;
  }
  .tag-tail {
    position: absolute;
    left: 320px;
    top: 115px;
    width: 23px;
    height: 23px;
  }
  .contact-line {
    position: absolute;
    left: 50px;
    right: 42px;
    top: 369px;
    display: flex;
    align-items: center;
    justify-content: space-between;
    font-size: 15px;
    font-weight: 400;
    color: var(--ink);
    white-space: nowrap;
  }
  .contact-line .divider {
    flex: 0 0 13px;
    width: 13px;
    height: 13px;
    border: 3px solid var(--dot-grey);
    border-radius: 50%;
  }
  .brand-name {
    font-weight: 500;
    font-size: 30px;
    letter-spacing: 1px;
    color: var(--paper-text);
  }
</style>
</head>
<body>
<main class="canvas">
  <section class="card card-front" aria-label="Business card front">
    <div class="name-tag">
      <div class="person-name">Mara Kessler</div>
      <div class="person-title">Sales Manager</div>
    </div>
    <svg class="tag-tail" viewBox="0 0 23 23" aria-hidden="true">
      <polygon points="0,0 23,0 23,23" fill="#000"/>
    </svg>
    <div class="contact-line">
      <span class="phone">987.654.321</span>
      <span class="divider"></span>
      <span class="email">mara@velmora-example.com</span>
      <span class="divider"></span>
      <span class="website">www.velmoraandco-example.com</span>
    </div>
  </section>

  <section class="card card-back" aria-label="Business card back">
    <div class="brand-name">VELMORA &amp; CO</div>
  </section>
</main>
</body>
</html>
```